Speisekarten-Design für Biergarten am Ufer des Bodensees
Super tolle Designerin. Vielen Dank Roswitha!
Zielgruppe
Wir sind ein direkt am Ufer des Bodensees liegender Biergarten, welcher seit über 30 Jahren besteht und deshalb fest in unserer Stadt verwurzelt ist. Zu unserer Zielgruppe gehören Touristen und Einheimische jeglicher Art - wir heißen einfach alle willkommen. Wir bieten unseren Gästen einfache Speisen und lokale Getränke. Uns ist wichtig, dass die Speise- & Getränkekarte das Gefühl von Heimat, Regionalität und Liebe zum Bodensee vermittelt. Wir bevorzugen ein modernes und klares Design, welches jedoch klassische Strukturen wie die eines typischen 60er-Jahre-Diners miteinbezieht.
Aufgabenstellung
Es wäre es toll, wenn diese Faltbar und kompakt (DIN-A4 evtl. etwas größer) ist. Die Textfelder sollten das komplette Speise- und Getränkeangebot darstellen (ca. 15 Gerichte, 6 Biersorten, 6 Softdrinks, 6 Heißgetränke). Wir bevorzugen warme Farbtöne. Es ist nicht notwendig Bilder in der Karte zu hinterlegen.

```html
<!DOCTYPE html>
<html lang="de">
<head>
<meta charset="utf-8">
<title>Biergarten – Speisekarte</title>
<link rel="stylesheet" href="https://fonts.googleapis.com/css2?family=Roboto:wght@300&family=Source+Sans+3:wght@400;600;700&display=swap">
<style>
  :root {
    --teal: #0a7396;
    --paper: #fbf8ee;
    --frame: #cfcabb;
    --ink: #1f1f1f;
    --hop-light: #d9d7d0;
    --hop-dark: #a9a7a1;
    --hop-faint: #efebdd;
    --stage: #ffffff;
  }
  * { box-sizing: border-box; margin: 0; padding: 0; }
  html, body { width: 1200px; height: 569px; overflow: hidden; background: var(--stage); }
  body { position: relative; font-family: "Source Sans 3", Arial, sans-serif; color: var(--ink); }

  /* ---------- Cover ---------- */
  .cover {
    position: absolute; left: 40px; top: 37px; width: 358px; height: 498px;
    background: var(--paper); border: 1px solid var(--frame);
  }
  .cover__pattern {
    position: absolute; inset: 24px 20px;
    background:
      radial-gradient(circle at 50% 50%, var(--hop-dark) 0 9px, transparent 13px) 0 0 / 55px 63px,
      var(--paper);
    opacity: .55;
  }
  .cover__seal {
    position: absolute; left: 77px; top: 184px; width: 202px; height: 202px;
    border-radius: 50%; background: var(--teal);
    display: flex; flex-direction: column; align-items: center; justify-content: center;
    color: #fff; font-family: "Roboto", Arial, sans-serif; font-weight: 300;
  }
  .cover__seal::before {
    content: ""; position: absolute; inset: 8px; border-radius: 50%;
    border: 1px dashed rgba(255,255,255,.85);
  }
  .cover__title-top { font-size: 51px; line-height: 1; letter-spacing: 3px; }
  .cover__title-bottom { font-size: 29px; line-height: 1.1; letter-spacing: 1.5px; margin-top: 4px; }

  /* ---------- Inner spread ---------- */
  .spread {
    position: absolute; left: 449px; top: 37px; width: 711px; height: 498px;
    background: var(--paper); border: 1px solid var(--frame); overflow: hidden;
  }
  .spread__backdrop {
    position: absolute; inset: 0;
    background:
      radial-gradient(ellipse 90px 110px at 60px 470px, var(--hop-faint), transparent 70%),
      radial-gradient(ellipse 110px 80px at 360px 10px, var(--hop-faint), transparent 70%),
      radial-gradient(ellipse 90px 120px at 680px 470px, var(--hop-faint), transparent 70%);
  }
  .fold {
    position: absolute; left: 804px; top: 30px; height: 525px;
    border-left: 1px dashed #9b9b9b;
  }

  .section-title {
    position: absolute; color: var(--teal); font-weight: 700;
    font-size: 21px; letter-spacing: 2px;
    transform: rotate(-90deg); transform-origin: left top; white-space: nowrap;
  }
  .rule { position: absolute; width: 0; border-left: 2px dotted var(--teal); }

  .dish-column { position: absolute; width: 119px; }
  .dish { margin-bottom: 8px; }
  .dish__head, .drink {
    display: flex; align-items: baseline; white-space: nowrap;
  }
  .dish__head { font-size: 9px; line-height: 11px; }
  .dish__name { color: var(--teal); font-weight: 700; }
  .leader { flex: 1; border-bottom: 1px dotted #555; margin: 0 1px; transform: translateY(-2px); min-width: 4px; }
  .dish__price { color: var(--ink); }
  .dish__text { font-size: 7.1px; line-height: 9.3px; }

  .drink-group { position: absolute; left: 871px; width: 118px; }
  .drink-group__title {
    color: var(--teal); font-weight: 700; font-size: 8.6px; line-height: 11px;
    padding-bottom: 3px; border-bottom: 2px dotted var(--teal); margin-bottom: 3px;
  }
  .drink { font-size: 7px; line-height: 14.4px; font-weight: 700; text-transform: uppercase; }
  .drink .leader { font-weight: 400; }
  .drink__price { font-weight: 400; font-size: 7.6px; }

  .hop-column {
    position: absolute; left: 1033px; top: 115px; width: 84px; height: 300px;
    background:
      radial-gradient(circle at 50% 50%, var(--hop-dark) 0 10px, transparent 15px) 0 0 / 42px 63px;
    opacity: .6;
  }
  .note {
    position: absolute; left: 1033px; top: 426px; width: 84px;
    font-size: 6.6px; line-height: 9px; text-align: justify;
  }
</style>
</head>
<body>
  <section class="cover">
    <div class="cover__pattern" role="img" aria-label="Gezeichnetes Muster aus Hopfendolden in grauen Tönen"></div>
    <div class="cover__seal">
      <span class="cover__title-top">BIER</span>
      <span class="cover__title-bottom">GARTEN</span>
    </div>
  </section>

  <section class="spread">
    <div class="spread__backdrop" role="img" aria-label="Blasse, große Hopfenzeichnungen als Hintergrund"></div>
  </section>
  <div class="fold"></div>

  <h2 class="section-title" style="left:476px; top:250px;">GERICHTE</h2>
  <div class="rule" style="left:504px; top:117px; height:346px;"></div>
  <div class="rule" style="left:644px; top:117px; height:346px;"></div>

  <div class="dish-column" style="left:513px; top:115px;">
    <div class="dish"><div class="dish__head"><span class="dish__name">Toast Hawaii</span><span class="leader"></span><span class="dish__price">4.50</span></div><p class="dish__text">Lorem ipsum dolor amet, consectetur adipiscing elit, sed do eiusmod tempor incididunt ut labore et dolore</p></div>
    <div class="dish"><div class="dish__head"><span class="dish__name">Grillteller</span><span class="leader"></span><span class="dish__price">7.50</span></div><p class="dish__text">Ut enim ad minim veniam, quis nostrud exercitation ullamco laboris</p></div>
    <div class="dish"><div class="dish__head"><span class="dish__name">Gemischter Salat</span><span class="leader"></span><span class="dish__price">4.50</span></div><p class="dish__text">Ut enim ad minim veniam, quis nostrud exercitation ullamco laboris nisi ut aliquip ex ea commodo consequat nisi ut lorem ipsum</p></div>
    <div class="dish"><div class="dish__head"><span class="dish__name">Wurstteller</span><span class="leader"></span><span class="dish__price">4.00</span></div><p class="dish__text">Lorem ipsum dolor sit, consectetur alaboris nisi ut aliquip ex</p></div>
    <div class="dish"><div class="dish__head"><span class="dish__name">Toast Hawaii</span><span class="leader"></span><span class="dish__price">4.50</span></div><p class="dish__text">Lorem ipsum dolor amet, consectetur adipiscing elit, sed do eiusmod tempor incididunt ut labore aliqua</p></div>
    <div class="dish"><div class="dish__head"><span class="dish__name">Grillteller</span><span class="leader"></span><span class="dish__price">7.50</span></div><p class="dish__text">Ut enim ad minim veniam, quis nostrud exercitation ullamco laboris nisi ut aliquip ex ea commodo ut enim laborem</p></div>
    <div class="dish"><div class="dish__head"><span class="dish__name">Gemischter Salat</span><span class="leader"></span><span class="dish__price">4.50</span></div><p class="dish__text">Ut enim ad minim veniam, quis nostrud exercitation ullamco laboris nisi ut aliquip ex</p></div>
    <div class="dish"><div class="dish__head"><span class="dish__name">Grillteller</span><span class="leader"></span><span class="dish__price">7.50</span></div><p class="dish__text">Ut enim ad minim veniam, quis nostrud exercitation ullamco laboris nisi ut aliquip ex ea commodo</p></div>
  </div>

  <div class="dish-column" style="left:656px; top:115px;">
    <div class="dish"><div class="dish__head"><span class="dish__name">Toast Hawaii</span><span class="leader"></span><span class="dish__price">4.50</span></div><p class="dish__text">Lorem ipsum dolor amet, consectetur adipiscing elit, sed do eiusmod</p></div>
    <div class="dish"><div class="dish__head"><span class="dish__name">Grillteller</span><span class="leader"></span><span class="dish__price">7.50</span></div><p class="dish__text">Ut enim ad minim veniam, quis nostrud exercitation ullamco laboris nisi ut aliquip ex ea commodo</p></div>
    <div class="dish"><div class="dish__head"><span class="dish__name">Gemischter Salat</span><span class="leader"></span><span class="dish__price">4.50</span></div><p class="dish__text">Ut enim ad minim veniam, quis nostrud exercitation ullamco laboris nisi ut aliquip ex ea commodo consequat nisi ut lorem ipsum</p></div>
    <div class="dish"><div class="dish__head"><span class="dish__name">Wurstteller</span><span class="leader"></span><span class="dish__price">4.00</span></div><p class="dish__text">Lorem ipsum dolor sit, consectetur adipiscing elit, sed do eiusmod</p></div>
    <div class="dish"><div class="dish__head"><span class="dish__name">Grillteller</span><span class="leader"></span><span class="dish__price">7.50</span></div><p class="dish__text">Ut enim ad minim veniam, quis nostrud exercitation ullamco laboris nisi ut aliquip ex ea commodo</p></div>
    <div class="dish"><div class="dish__head"><span class="dish__name">Toast Hawaii</span><span class="leader"></span><span class="dish__price">4.50</span></div><p class="dish__text">Ut enim ad minim veniam, quis nostrud exercitation tempor incididunt ut labore aliqua</p></div>
    <div class="dish"><div class="dish__head"><span class="dish__name">Gemischter Salat</span><span class="leader"></span><span class="dish__price">4.50</span></div><p class="dish__text">Ut enim ad minim veniam, quis nostrud exercitation ullamco laboris nisi ut aliquip ex ea commodo consequat ullamco laboris nostrud</p></div>
    <div class="dish"><div class="dish__head"><span class="dish__name">Grillteller</span><span class="leader"></span><span class="dish__price">7.50</span></div><p class="dish__text">Ut enim ad minim veniam, quis nostrud exercitation ullamco laboris nisi ut aliquip ex ea commodo</p></div>
  </div>

  <h2 class="section-title" style="left:835px; top:262px;">GETRÄNKE</h2>
  <div class="rule" style="left:861px; top:117px; height:346px;"></div>
  <div class="rule" style="left:1001px; top:117px; height:346px;"></div>

  <div class="drink-group" style="top:115px;">
    <h3 class="drink-group__title">Etwas Heisses</h3>
    <div class="drink"><span>Kaffee</span><span class="leader"></span><span class="drink__price">4.50</span></div>
    <div class="drink"><span>Milchkaffee</span><span class="leader"></span><span class="drink__price">4.50</span></div>
    <div class="drink"><span>Teekanne</span><span class="leader"></span><span class="drink__price">4.00</span></div>
    <div class="drink"><span>Kaffee Schnaps</span><span class="leader"></span><span class="drink__price">4.00</span></div>
    <div class="drink"><span>Grog</span><span class="leader"></span><span class="drink__price">4.00</span></div>
    <div class="drink"><span>Schokolade</span><span class="leader"></span><span class="drink__price">4.00</span></div>
  </div>

  <div class="drink-group" style="top:238px;">
    <h3 class="drink-group__title">Etwas Kaltes</h3>
    <div class="drink"><span>Kola Rot</span><span class="leader"></span><span class="drink__price">4.50</span></div>
    <div class="drink"><span>Zitrosa</span><span class="leader"></span><span class="drink__price">4.50</span></div>
    <div class="drink"><span>Oranja</span><span class="leader"></span><span class="drink__price">4.00</span></div>
    <div class="drink"><span>Seequell</span><span class="leader"></span><span class="drink__price">4.00</span></div>
    <div class="drink"><span>Ginger Ale</span><span class="leader"></span><span class="drink__price">4.00</span></div>
    <div class="drink"><span>Tonic Blau</span><span class="leader"></span><span class="drink__price">4.00</span></div>
  </div>

  <div class="drink-group" style="top:361px;">
    <h3 class="drink-group__title">Verschiedene Biere</h3>
    <div class="drink"><span>Lager</span><span class="leader"></span><span class="drink__price">4.50</span></div>
    <div class="drink"><span>Draft</span><span class="leader"></span><span class="drink__price">4.50</span></div>
    <div class="drink"><span>Hafenbräu</span><span class="leader"></span><span class="drink__price">4.00</span></div>
    <div class="drink"><span>Sonnenbräu</span><span class="leader"></span><span class="drink__price">4.00</span></div>
    <div class="drink"><span>Weizenhof</span><span class="leader"></span><span class="drink__price">4.50</span></div>
    <div class="drink"><span>Nordkrone</span><span class="leader"></span><span class="drink__price">4.50</span></div>
  </div>

  <div class="hop-column" role="img" aria-label="Zwei Reihen gezeichneter Hopfendolden"></div>
  <p class="note">Bei Fragen oder Menu-Anpassungen sprechen Sie bitte unser Personal auf Ihre Wünsche an</p>
</body>
</html>
```